Biz Card Design TPVC

New business card for a new company.
Logo was completed by a designer on ArtFlock and looking to continue requesting additional services.
Company Name: Tidal Prime Voltage Collective
Although this company is starting in Canada, we will be moving towards a global presence within the next 6 months.
Key elements to this business are as follows.
Energy Procurement
Energy Reduction Services
Demand Side Consulting
Energy Efficiency Consulting
Saving Clients Money
Helping Them Go "Green"
Managing Their Energy Requirements
Basically the goal for our company is to find the best procurement solution for our clients and reduce their energy consumption. This reduces their expenses and the amount of greenhouse gas they produce on a daily basis.
I have been in the energy footprint for the last 20 years and know that most companies are looking to "do whatever is necessary to get them to sign on the dotted line". I would prefer to walk away from a client that I can't help than to put them into a situation that they will regret for years to come. This is where the "TIDAL" part of the company name comes from.
The following is a catch phrase that encompasses what we do.
"Reducing your carbon footprint & energy bill at the same time!"
The back of the card needs to have this statement along with some sort of illustration. The back is a playground for creative ideas.
The front of the card needs the following.
Logo.
First & Last Name (Gus Marwick)
Title (Energy Warrior)
Phone Number (555) 314-2768
Fax Number (555) 862-4091
Email Address gus@tidalprimevoltage.example
Address 47 Orchard Lane Toronto Ontario K4P 2Z7
I want it to be a card that is remembered when any of my staff give it to a customer. It HAS to stand out.
Target Market(s)
Business Owners, Decision Makers, 30 to 65+
Industry/Entity Type
Business
Look and feel
Each slider illustrates characteristics of the customer's brand and the style your logo design should communicate.

```html
<!DOCTYPE html>
<html lang="en">
<head>
<meta charset="utf-8">
<title>Tidal Prime Voltage Collective — Business Card</title>
<link href="https://fonts.googleapis.com/css2?family=Exo+2:wght@400;600&display=swap" rel="stylesheet">
<style>
  :root {
    --backdrop: #2b2b2b;
    --card-yellow: #ffcc00;
    --card-black: #000000;
    --brand-blue: #3f6fb0;
    --brand-green: #34a13f;
    --text-font: "Exo 2", sans-serif;
  }
  html, body {
    margin: 0;
    padding: 0;
    width: 1200px;
    height: 900px;
    overflow: hidden;
    background: var(--backdrop);
    font-family: var(--text-font);
  }
  .canvas {
    position: relative;
    width: 1200px;
    height: 900px;
  }
  .card {
    position: absolute;
    top: 308px;
    width: 513px;
    height: 284px;
    border-radius: 22px;
    overflow: hidden;
    background: var(--card-black);
    display: flex;
    flex-direction: column;
  }
  .card--back { left: 72px; }
  .card--front { left: 615px; }
  .card__band {
    height: 142px;
    background: var(--card-yellow);
    display: flex;
    flex-direction: column;
    align-items: center;
    justify-content: center;
    text-align: center;
  }
  .card__base {
    flex: 1;
    display: flex;
    flex-direction: column;
    align-items: center;
    justify-content: center;
    text-align: center;
  }
  .tagline {
    margin: 0;
    color: var(--brand-blue);
    font-weight: 600;
    font-size: 16px;
    line-height: 1.2;
  }
  .brand {
    display: flex;
    align-items: center;
    gap: 8px;
  }
  .brand__dot {
    width: 14px;
    height: 14px;
    border-radius: 50%;
    background: var(--brand-green);
  }
  .brand__name {
    color: var(--brand-blue);
    font-weight: 600;
    font-size: 19px;
    letter-spacing: 0.2px;
  }
  .card--front .card__band { justify-content: flex-end; padding-bottom: 30px; box-sizing: border-box; }
  .person__name {
    margin: 0;
    color: var(--brand-green);
    font-weight: 400;
    font-size: 21px;
    line-height: 1.1;
  }
  .person__title {
    margin: 2px 0 12px;
    color: var(--brand-green);
    font-size: 14px;
  }
  .contact {
    margin: 0;
    color: var(--brand-blue);
    font-size: 11px;
    line-height: 1.3;
    font-style: normal;
  }
</style>
</head>
<body>
<main class="canvas">
  <section class="card card--back" aria-label="Card back">
    <div class="card__band">
      <p class="tagline">Reducing your carbon footprint<br>and your energy bill at the same time!</p>
    </div>
    <div class="card__base">
      <div class="brand">
        <span class="brand__dot"></span>
        <span class="brand__name">Tidal Prime Voltage Collective</span>
      </div>
    </div>
  </section>

  <section class="card card--front" aria-label="Card front">
    <div class="card__band">
      <div class="brand">
        <span class="brand__dot"></span>
        <span class="brand__name">Tidal Prime Voltage Collective</span>
      </div>
    </div>
    <div class="card__base">
      <h1 class="person__name">Gus Marwick</h1>
      <p class="person__title">Energy Warrior</p>
      <address class="contact">
        Address 47 Orchard Lane Toronto Ontario K4P 2Z7<br>
        Phone (555) 314-2768<br>
        Fax (555) 862-4091<br>
        Email gus@tidalprimevoltage.example
      </address>
    </div>
  </section>
</main>
</body>
</html>
```